K8 FIRST WEBSITE FOR CONCRETE DESIGN START-UP

We would like a 3-4 page website. Very basic. About Us, Pricing, Testimonials, Pictures and somewhere they can contact us. We are a concrete design/epoxy company. Want clean/modern and something that is user friendly that we can keep building on. Important we can update the website and that it shows good examples of our work.
Target Market(s)
Home owners or business owners who want unique solutions to concrete flooring in garages, patios, basements, showrooms or anywhere concrete is or can be.
Industry/Entity Type
Concrete
Coding
Coded - Design and coding required
Number of Pages Required
4 page

```html
<!DOCTYPE html>
<html lang="en">
<head>
<meta charset="utf-8">
<title>K8 Concrete — Coating &amp; Polished Concrete</title>
<link href="https://fonts.googleapis.com/css2?family=Saira:wght@500;600;700&family=Lato:ital,wght@0,400;0,700;1,400&display=swap" rel="stylesheet">
<style>
:root{
  --orange:#f47b20;
  --orange-light:#f7931e;
  --ink:#111111;
  --text:#444444;
  --grey:#a6a8ad;
  --panel:#dcdcdc;
  --white:#ffffff;
  --line:#c8c8c8;
}
*{margin:0;padding:0;box-sizing:border-box}
html,body{width:1200px;height:3102px;overflow:hidden;background:var(--white)}
body{position:relative;font-family:'Lato',sans-serif;color:var(--text)}
a{text-decoration:none}
.abs{position:absolute}
.display{font-family:'Saira',sans-serif;font-weight:600;color:var(--ink)}

/* header */
.site-header{position:absolute;left:0;top:0;width:1200px;height:91px;background:var(--white);z-index:3}
.brand{position:absolute;left:162px;top:18px;width:205px;height:102px;background:var(--white);
  clip-path:polygon(18% 0,100% 0,82% 100%,0 100%);display:flex;align-items:center;justify-content:center;
  text-decoration:none}
.brand-name{font-family:'Saira',sans-serif;font-weight:700;font-size:22px;line-height:1;color:var(--ink);
  letter-spacing:1px;white-space:nowrap}
.phone{position:absolute;right:137px;top:14px;font-family:'Saira',sans-serif;font-weight:600;font-size:20px;color:var(--ink);display:flex;align-items:center;gap:6px}
.main-nav{position:absolute;right:138px;top:50px;display:flex;gap:38px}
.main-nav a{font-family:'Saira',sans-serif;font-weight:600;font-size:15px;color:var(--ink);padding-bottom:8px}
.main-nav a.active{color:var(--orange);border-bottom:2px solid var(--ink)}

/* hero */
.hero{position:absolute;left:0;top:91px;width:1200px;height:613px;
  background:linear-gradient(180deg,#8b8e92 0%,#5d6166 30%,#2c2f35 55%,#3a3f4a 75%,#55657a 100%);
  clip-path:polygon(0 0,100% 0,100% 100%,0 89%)}
.hero-text{position:absolute;left:0;top:195px;width:1200px;text-align:center;color:var(--white)}
.hero-text h1{font-family:'Saira',sans-serif;font-weight:600;font-size:55px;line-height:66px}
.hero-text h2{font-family:'Saira',sans-serif;font-weight:500;font-size:31px;line-height:40px;margin-top:2px}
.btn{display:inline-block;background:linear-gradient(180deg,var(--orange-light),#f26522);color:var(--white);
  font-family:'Saira',sans-serif;font-weight:600}
.hero .btn{position:absolute;left:508px;top:324px;width:191px;height:56px;line-height:56px;text-align:center;font-size:19px}
.arrow{position:absolute;width:30px;height:56px}

/* about */
.section-title{position:absolute;left:0;width:1200px;text-align:center;font-family:'Saira',sans-serif;font-weight:600;font-size:34px;color:var(--ink)}
.about-lead{position:absolute;left:220px;top:816px;width:760px;text-align:center;font-size:17px;line-height:27px;color:#555}
.service{position:absolute;width:300px}
.service h3{font-family:'Saira',sans-serif;font-weight:600;font-size:21px;color:var(--ink);line-height:26px}
.service p{font-size:12.5px;line-height:19px;color:#555;margin-top:6px}
.service.left{left:118px;text-align:right}
.service.right{left:764px;text-align:left}
.dot{position:absolute;width:14px;height:14px;border-radius:50%;background:var(--orange)}
.emblem{position:absolute;left:463px;top:1023px;width:247px;height:111px;display:flex;align-items:center;justify-content:center;
  font-family:'Saira',sans-serif;font-weight:700;font-size:100px;color:#555a60}

/* gallery */
.gallery-title{color:var(--white)}
.tile{position:absolute}

/* testimonials */
.testimonial{position:absolute;top:2122px;width:420px;height:207px;border:2px solid var(--line);border-radius:4px 24px 24px 24px;background:var(--white);
  box-shadow:0 2px 4px rgba(0,0,0,.15)}
.avatar{position:absolute;left:25px;top:29px;width:74px;height:78px;border-radius:10px;background:linear-gradient(160deg,#d8cfc6,#6b5a4f)}
.quote-mark{position:absolute;left:112px;top:26px;font-family:'Saira',sans-serif;font-weight:700;font-size:42px;color:var(--orange);font-style:italic;line-height:40px}
.testimonial p{position:absolute;left:146px;top:33px;width:250px;font-style:italic;font-size:14px;line-height:21.5px;color:#333}
.testimonial .author{position:absolute;left:146px;top:152px;font-weight:700;font-size:14px;color:var(--orange)}

/* contact */
.contact-panel{position:absolute;left:0;top:2393px;width:1200px;height:600px;background:var(--panel)}
.contact-photo{position:absolute;left:692px;top:2420px;width:508px;height:553px;
  background:linear-gradient(135deg,#c7b79f 0%,#e8e6e2 35%,#9a9894 70%,#5e5a55 100%);
  clip-path:polygon(0 0,100% 3%,100% 100%,0 98%)}
.field{position:absolute;left:161px;width:396px;height:44px;background:var(--white);border:1px solid #bdbdbd;
  font-size:15px;color:#555;padding:13px 0 0 17px;display:flex;gap:6px;align-items:flex-start}
.field svg{margin-top:2px}
.submit{position:absolute;left:162px;top:2810px;width:133px;height:42px;line-height:42px;text-align:center;font-size:17px}

/* footer */
.footer-nav{position:absolute;left:186px;top:2998px;display:flex;gap:38px}
.footer-nav a{font-family:'Saira',sans-serif;font-weight:600;font-size:15px;color:var(--ink)}
.social{position:absolute;left:889px;top:3002px;display:flex;gap:29px}
.social span{width:14px;height:14px;border-radius:50%;background:var(--ink);display:block}
.copyright{position:absolute;left:186px;top:3037px;font-size:14px;color:#333}
</style>
</head>
<body>

<header class="site-header">
  <a class="brand" href="#"><span class="brand-name">K8 CONCRETE</span></a>
  <div class="phone">
    <svg width="18" height="18" viewBox="0 0 24 24" aria-hidden="true"><path fill="#f47b20" d="M6.6 10.8a15.1 15.1 0 0 0 6.6 6.6l2.2-2.2c.3-.3.7-.4 1-.2 1.1.4 2.3.6 3.6.6.6 0 1 .4 1 1V20c0 .6-.4 1-1 1A17 17 0 0 1 3 4c0-.6.4-1 1-1h3.5c.6 0 1 .4 1 1 0 1.3.2 2.5.6 3.6.1.3 0 .7-.2 1z"/></svg>
    555-014-2290
  </div>
  <nav class="main-nav">
    <a class="active" href="#">HOME</a>
    <a href="#">ABOUT US</a>
    <a href="#">PRICING</a>
    <a href="#">TESTIMONIALS</a>
    <a href="#">GALLERY</a>
    <a href="#">CONTACT US</a>
  </nav>
</header>

<section class="hero" role="img" aria-label="Photo of a glossy epoxy-coated floor in an empty room reflecting the windows">
  <svg class="arrow" style="left:111px;top:240px" viewBox="0 0 30 56" aria-hidden="true"><polyline points="27,2 3,28 27,54" fill="none" stroke="#fff" stroke-width="3"/></svg>
  <svg class="arrow" style="left:1061px;top:240px" viewBox="0 0 30 56" aria-hidden="true"><polyline points="3,2 27,28 3,54" fill="none" stroke="#fff" stroke-width="3"/></svg>
  <div class="hero-text">
    <h1>WELCOME TO K8 CONCRETE</h1>
    <h2>COATING &amp; POLISHED CONCRETE</h2>
  </div>
  <a class="btn" href="#">READ MORE</a>
</section>

<h2 class="section-title" style="top:750px">ABOUT K8 CONCRETE</h2>
<p class="about-lead">Pellentesque faucibus Ut accumsan ultricies elit Maecenas at justo id velit placerat molestie Donec dictum lectus non odio Cras a ante vitae enim iaculis aliquam Mauris nunc &nbsp; est nunc venenatis in tristique eu imperdiet ac nisl Cum sociis natoque penatibus</p>

<svg class="abs" style="left:0;top:950px" width="1200" height="270" aria-hidden="true">
  <line x1="448" y1="15" x2="448" y2="252" stroke="#c8c8c8" stroke-width="1.5"/>
  <line x1="740" y1="15" x2="740" y2="252" stroke="#c8c8c8" stroke-width="1.5"/>
  <line x1="448" y1="123" x2="503" y2="123" stroke="#c8c8c8" stroke-width="1.5"/>
  <line x1="700" y1="123" x2="740" y2="123" stroke="#c8c8c8" stroke-width="1.5"/>
</svg>
<span class="dot" style="left:441px;top:958px"></span>
<span class="dot" style="left:441px;top:1066px"></span>
<span class="dot" style="left:441px;top:1196px"></span>
<span class="dot" style="left:733px;top:958px"></span>
<span class="dot" style="left:733px;top:1066px"></span>
<span class="dot" style="left:733px;top:1196px"></span>

<div class="emblem">K8</div>

<div class="service left" style="top:946px"><h3>COATING</h3><p>itae enim iaculis aliquam Mauris nunc est nunc<br>venenatis in tristique eu imperdiet ac nisl</p></div>
<div class="service left" style="top:1057px"><h3>EPOXY</h3><p>itae enim iaculis aliquam Mauris nunc est nunc<br>venenatis in tristique eu imperdiet ac nisl</p></div>
<div class="service left" style="top:1184px"><h3>FLAT WORK</h3><p>itae enim iaculis aliquam Mauris nunc est nunc<br>venenatis in tristique eu imperdiet ac nisl</p></div>
<div class="service right" style="top:946px"><h3>POLISHED CONCRETE</h3><p>itae enim iaculis aliquam Mauris nunc est nunc<br>venenatis in tristique eu imperdiet ac nisl</p></div>
<div class="service right" style="top:1057px"><h3>CUTTING</h3><p>itae enim iaculis aliquam Mauris nunc est nunc<br>venenatis in tristique eu imperdiet ac nisl</p></div>
<div class="service right" style="top:1184px"><h3>CORING</h3><p>itae enim iaculis aliquam Mauris nunc est nunc<br>venenatis in tristique eu imperdiet ac nisl</p></div>

<svg class="abs" style="left:0;top:1290px" width="1200" height="750" aria-hidden="true">
  <polygon points="0,22 410,70 0,106" fill="#a6a8ad"/>
  <polygon points="1200,635 1200,698 700,665" fill="#a6a8ad"/>
  <polygon points="0,106 1200,4 1200,636 0,738" fill="#f47b20"/>
</svg>
<h2 class="section-title gallery-title" style="top:1401px">OUR GALLERY</h2>
<div class="tile" style="left:168px;top:1485px;width:330px;height:390px;background:linear-gradient(160deg,#6d6a66,#b7b3ad 45%,#8d8983)" role="img" aria-label="Polished concrete floor with grinding machine"></div>
<div class="tile" style="left:510px;top:1485px;width:170px;height:187px;background:linear-gradient(150deg,#3b2f28,#8b5a35 50%,#4a3a30)" role="img" aria-label="Metallic copper epoxy floor detail"></div>
<div class="tile" style="left:690px;top:1485px;width:349px;height:187px;background:linear-gradient(160deg,#4a4540,#7a6c5e 50%,#3d3834)" role="img" aria-label="Close-up of exposed aggregate polished concrete"></div>
<div class="tile" style="left:510px;top:1688px;width:170px;height:187px;background:linear-gradient(160deg,#2a2a2c,#7d7d80 50%,#1e1e20)" role="img" aria-label="Black and white marbled epoxy floor"></div>
<div class="tile" style="left:690px;top:1688px;width:170px;height:187px;background:linear-gradient(160deg,#dfe6ee,#8c9db0 50%,#e9eef3)" role="img" aria-label="White and blue marble-effect epoxy finish"></div>
<div class="tile" style="left:869px;top:1688px;width:170px;height:187px;background:linear-gradient(160deg,#3c4148,#8a9099 50%,#2c3036)" role="img" aria-label="Floor grinding equipment close-up"></div>

<h2 class="section-title" style="top:2055px">TESTIMONIALS</h2>
<svg class="arrow" style="left:108px;top:2188px" viewBox="0 0 30 56" aria-hidden="true"><polyline points="27,2 3,28 27,54" fill="none" stroke="#555" stroke-width="2"/></svg>
<svg class="arrow" style="left:1060px;top:2188px" viewBox="0 0 30 56" aria-hidden="true"><polyline points="3,2 27,28 3,54" fill="none" stroke="#555" stroke-width="2"/></svg>

<article class="testimonial" style="left:172px">
  <div class="avatar" role="img" aria-label="Customer portrait"></div>
  <span class="quote-mark">"</span>
  <p>Pellentesque faucibus Ut accumsan ultricies elit Maecenas at justo id velit placerat molestie Donec dictum lectus non odio Cras a ante vitae enim iaculis aliquam Mauris nunc quam</p>
  <span class="author">BY AUTHOR NAME</span>
</article>
<article class="testimonial" style="left:609px;top:2119px">
  <div class="avatar" role="img" aria-label="Customer portrait" style="background:linear-gradient(160deg,#c9b7a4,#4a4038)"></div>
  <span class="quote-mark">"</span>
  <p>Pellentesque faucibus Ut accumsan ultricies elit Maecenas at justo id velit placerat molestie Donec dictum lectus non odio Cras a ante vitae enim iaculis aliquam Mauris nunc quam</p>
  <span class="author">BY AUTHOR NAME</span>
</article>

<div class="contact-panel"></div>
<div class="contact-photo" role="img" aria-label="Worker operating a floor polishing machine indoors"></div>
<svg class="abs" style="left:0;top:2915px" width="1200" height="80" aria-hidden="true">
  <polygon points="0,6 380,20 0,66" fill="#f47b20"/>
  <polygon points="0,66 380,20 1200,54 1200,80 0,80" fill="#ffffff"/>
</svg>
<h2 class="abs display" style="left:160px;top:2480px;font-size:29px">CONTACT US</h2>
<div class="field" style="top:2543px">
  <svg width="13" height="14" viewBox="0 0 16 16" aria-hidden="true"><circle cx="8" cy="4.5" r="3.5" fill="#777"/><path d="M1 16c0-4 3-7 7-7s7 3 7 7z" fill="#777"/></svg>Name</div>
<div class="field" style="top:2595px">
  <svg width="14" height="12" viewBox="0 0 16 12" aria-hidden="true"><rect width="16" height="12" fill="#777"/><polyline points="0,0 8,7 16,0" fill="none" stroke="#fff" stroke-width="1.5"/></svg>Email</div>
<div class="field" style="top:2647px">
  <svg width="13" height="13" viewBox="0 0 24 24" aria-hidden="true"><path fill="#777" d="M6.6 10.8a15.1 15.1 0 0 0 6.6 6.6l2.2-2.2c.3-.3.7-.4 1-.2 1.1.4 2.3.6 3.6.6.6 0 1 .4 1 1V20c0 .6-.4 1-1 1A17 17 0 0 1 3 4c0-.6.4-1 1-1h3.5c.6 0 1 .4 1 1 0 1.3.2 2.5.6 3.6.1.3 0 .7-.2 1z"/></svg>Phone</div>
<div class="field" style="top:2699px;height:100px;left:162px">Message</div>
<a class="btn submit" href="#">SUBMIT</a>

<nav class="footer-nav">
  <a href="#">HOME</a><a href="#">ABOUT US</a><a href="#">PRICING</a><a href="#">TESTIMONIALS</a><a href="#">GALLERY</a><a href="#">CONTACT US</a>
</nav>
<div class="social" aria-label="Social links"><span></span><span></span><span></span><span></span></div>
<p class="copyright">© 2019 Company Name &nbsp;All right reserved</p>

</body>
</html>
```